innovative investment real estate sales firm

We are a uniquely collabrative firm that seeks to bring a conultative approach to uncovering hidden opportunities for our clients, our website needs to convey our client focused approach. Our firm specializes in the sale of apartment properties in Southern California. We have a team of researchers, transaction coordinators and marketing personal to support our geographically specialized advisers. We need a website that introduces clients to our unique way of better helping them achieve their investment goals.

Target Market(s)

High net worth individuals and families

Industry/Entity Type

Real Estate Agent

Font styles to use
Other font styles liked:
• please use font provided

Requirements
Must have
• Stories of our recent projects
• Features on our people
• email capture for viewing inventory
• content that showcases our unique consultative approach that uncovers unrealized opportunities

```html
<!DOCTYPE html>
<html lang="en">
<head>
<meta charset="utf-8">
<title>Meridian — Why Choose, News & Team</title>
<link href="https://fonts.googleapis.com/css2?family=Montserrat:wght@600;700&family=Questrial&display=swap" rel="stylesheet">
<style>
  :root{
    --teal:#0ca3b7;
    --green:#99c31c;
    --ink:#485863;
    --muted:#8b8b8b;
    --sky:#daf0f4;
    --lime:#eff7da;
    --rule:#d6d6d6;
    --white:#ffffff;
  }
  *{margin:0;padding:0;box-sizing:border-box}
  html,body{width:1200px;height:979px;overflow:hidden;background:var(--white)}
  body{position:relative;font-family:"Questrial",sans-serif;color:var(--muted)}
  .abs{position:absolute}
  .panel{position:absolute;top:0;height:458px;width:600px}
  .panel--why{left:0;background:var(--sky)}
  .panel--news{left:600px;background:var(--lime)}
  .section-title{position:absolute;font-family:"Montserrat",sans-serif;font-weight:700;font-size:29px;letter-spacing:-0.3px;color:var(--ink);text-align:center;white-space:nowrap;transform:translateX(-50%)}
  .divider{position:absolute;height:2px;background:var(--white)}
  .divider span{position:absolute;top:0;height:2px}
  .feature-title{position:absolute;font-size:17px;color:var(--teal);white-space:nowrap}
  .feature-text{position:absolute;font-size:13px;line-height:20px;color:var(--muted);width:290px}
  .nav-btn{position:absolute;width:25px;height:25px;display:flex;align-items:center;justify-content:center}
  .nav-btn svg{width:8px;height:8px}
  .post-image{position:absolute;left:681px;top:171px;width:137px;height:137px;border:1px solid #c9c9c9;background:linear-gradient(135deg,#f2f2f2,#d9d9d9)}
  .post-title{position:absolute;left:838px;top:166px;font-size:17px;color:var(--green);white-space:nowrap}
  .post-meta{position:absolute;left:838px;top:195px;font-size:11px;color:var(--muted);white-space:nowrap;display:flex;align-items:center;gap:4px}
  .post-meta .hl{color:var(--teal)}
  .post-text{position:absolute;left:838px;top:216px;width:270px;font-size:13px;line-height:20px}
  .read-more{position:absolute;left:838px;top:284px;font-size:13px;display:flex;align-items:center;gap:8px}
  .team-title{position:absolute;left:600px;top:532px;transform:translateX(-50%);font-family:"Montserrat",sans-serif;font-weight:700;font-size:29px;color:var(--green);white-space:nowrap}
  .team-divider{position:absolute;left:475px;top:580px;width:250px;height:2px;background:var(--rule)}
  .team-divider span{position:absolute;left:80px;width:90px;height:2px;background:var(--teal)}
  .member{position:absolute;top:624px;width:219px;text-align:center}
  .member-photo{width:219px;height:219px;position:relative}
  .member-photo .overlay{position:absolute;inset:0;background:rgba(72,88,99,.72);display:flex;align-items:center;justify-content:center}
  .member-name{margin-top:13px;font-size:17px;color:var(--teal)}
  .member-role{margin-top:6px;font-size:13px;color:var(--muted)}
  .carousel-arrow{position:absolute;top:722px}
</style>
</head>
<body>

<section class="panel panel--why"></section>
<section class="panel panel--news"></section>

<!-- Why choose -->
<h2 class="section-title" style="left:304px;top:74px">WHY CHOOSE MERIDIAN</h2>
<div class="divider" style="left:178px;top:127px;width:251px"><span style="left:81px;width:90px;background:var(--green)"></span></div>

<svg class="abs" style="left:124px;top:152px" width="68" height="68" viewBox="0 0 68 68" fill="none" stroke="var(--ink)" stroke-width="3" stroke-linecap="round" stroke-linejoin="round">
  <circle cx="27" cy="27" r="24"/>
  <path d="M45 45l6 6"/><path d="M50 49l10 10a3.5 3.5 0 0 1-5 5l-10-10z"/>
  <path d="M15 27l12-10 12 10" /><path d="M18 25v11h18v-11"/>
  <rect x="24" y="29" width="6" height="7" fill="var(--ink)"/>
</svg>
<div class="feature-title" style="left:209px;top:154px">Intelligent Researchers</div>
<div class="feature-text" style="left:209px;top:178px">Lnte neque, a lorem. Sed suscipit quam nisi, at suscipit lorem tincidunt ac.</div>

<svg class="abs" style="left:124px;top:252px" width="68" height="58" viewBox="0 0 68 58" fill="none" stroke="var(--ink)" stroke-width="3" stroke-linejoin="round">
  <path d="M44 12H6a4 4 0 0 0-4 4v34a4 4 0 0 0 4 4h46a4 4 0 0 0 4-4v-8"/>
  <path d="M56 34H44a5 5 0 0 0 0 10h12"/>
  <circle cx="54" cy="14" r="11"/>
  <text x="54" y="19" font-family="Questrial,sans-serif" font-size="13" fill="var(--ink)" stroke="none" text-anchor="middle">$</text>
</svg>
<div class="feature-title" style="left:209px;top:249px">Transaction Co-ordinators</div>
<div class="feature-text" style="left:209px;top:273px">Neque, a lorem. Sed suscipit quam nisi, at suscipit lorescipm ti dedncidunte</div>

<div class="nav-btn" style="left:275px;top:351px;background:var(--green)"><svg viewBox="0 0 8 8"><path d="M5 1L2 4l3 3" stroke="var(--ink)" fill="none"/></svg></div>
<div class="nav-btn" style="left:308px;top:351px;background:var(--green)"><svg viewBox="0 0 8 8"><path d="M3 1l3 3-3 3" stroke="var(--ink)" fill="none"/></svg></div>

<!-- News -->
<h2 class="section-title" style="left:900px;top:74px">NEWS &amp; BLOG</h2>
<div class="divider" style="left:775px;top:127px;width:250px"><span style="left:81px;width:90px;background:var(--teal)"></span></div>

<div class="post-image" role="img" aria-label="Businesswoman climbing white stairs beside a rising growth chart line"></div>
<div class="post-title">Uncovering hidden opportunities</div>
<div class="post-meta">
  <svg width="9" height="9" viewBox="0 0 10 10" fill="none" stroke="var(--ink)"><circle cx="5" cy="5" r="4"/><path d="M5 2.5V5h2"/></svg>
  <span class="hl">26th July, 2017</span>&nbsp;|&nbsp; Posted by: <span class="hl">Admin</span>
</div>
<div class="post-text">Lorem ipsum dolor sit amet, consectetur adipiscing elit. Quisque varius maximus magna, ac iaculis dui dictum non.</div>
<div class="read-more">Read More
  <svg width="10" height="8" viewBox="0 0 10 8" fill="none" stroke="var(--green)" stroke-width="1.5"><path d="M0 4h8M5 1l3 3-3 3"/></svg>
</div>

<div class="nav-btn" style="left:871px;top:351px;background:var(--teal)"><svg viewBox="0 0 8 8"><path d="M5 1L2 4l3 3" stroke="var(--ink)" fill="none"/></svg></div>
<div class="nav-btn" style="left:904px;top:351px;background:var(--teal)"><svg viewBox="0 0 8 8"><path d="M3 1l3 3-3 3" stroke="var(--ink)" fill="none"/></svg></div>

<!-- Team -->
<h2 class="team-title">OUR MERIDIAN TEAM</h2>
<div class="team-divider"><span></span></div>

<svg class="carousel-arrow" style="left:69px" width="16" height="24" viewBox="0 0 16 24" fill="none" stroke="var(--teal)" stroke-width="3.5"><path d="M12 3L4 12l8 9"/></svg>
<svg class="carousel-arrow" style="left:1116px" width="16" height="24" viewBox="0 0 16 24" fill="none" stroke="var(--teal)" stroke-width="3.5"><path d="M4 3l8 9-8 9"/></svg>

<div class="member" style="left:125px">
  <div class="member-photo" role="img" aria-label="Portrait of the chairman in a dark suit before a bookshelf" style="background:linear-gradient(160deg,#5a3a2e,#2b2a33 60%,#1d2230)"></div>
  <div class="member-name">Harlan T. Mercer</div>
  <div class="member-role">Chairman &amp; Founder</div>
</div>
<div class="member" style="left:369px">
  <div class="member-photo" role="img" aria-label="Portrait of the chief operating officer against a light wall" style="background:linear-gradient(160deg,#e4ddd2,#cfc6ba 55%,#3a3433)"></div>
  <div class="member-name">Elena R. Castillo</div>
  <div class="member-role">Chief Operating Officer</div>
</div>
<div class="member" style="left:612px">
  <div class="member-photo" role="img" aria-label="Portrait of the technical director in a plaid shirt" style="background:linear-gradient(160deg,#6f7d87,#4a5660)">
    <div class="overlay">
      <svg width="34" height="22" viewBox="0 0 34 22" fill="none" stroke="#ffffff" stroke-width="2"><path d="M2 11C7 4 12 2 17 2s10 2 15 9c-5 7-10 9-15 9S7 18 2 11z"/><circle cx="17" cy="11" r="5"/></svg>
    </div>
  </div>
  <div class="member-name">Owen D. Park</div>
  <div class="member-role">Technical Director</div>
</div>
<div class="member" style="left:857px">
  <div class="member-photo" role="img" aria-label="Portrait of the marketing head before a brick wall" style="background:linear-gradient(160deg,#9a8378,#6e5a52 55%,#2e2626)"></div>
  <div class="member-name">Sabrina L. Whitford</div>
  <div class="member-role">Marketing Head</div>
</div>

</body>
</html>
```